Bluefern Capital Counsel Needs a Letterhead

Tomi, we need a letterhead/banner for our blog, which is titled "Quiet Harbor Chronicle". The letterhead/banner should incorporate the enclosed banner image, logo, and the name of our blog ("Quiet Harbor Chronicle").

We would also like an alternative design that includes our picture. Here, we have two options that we would like to see.

In all, we would like to see 3 different designs: one banner without any pics; and two banner with two versions of our pictures.

The file size should be able to be resized for the space given to us at our website (http://bluefern-capital-counsel.com).

We also need the letterhead/banner by Friday, June 13. Thanks!!

```html
<!DOCTYPE html>
<html lang="en">
<head>
<meta charset="utf-8">
<title>Bluefern Capital Counsel LLC</title>
<link href="https://fonts.googleapis.com/css2?family=Arimo:ital,wght@0,400;0,700;1,400&family=Cinzel:wght@400&display=swap" rel="stylesheet">
<style>
:root{
  --night:#05070b;
  --sky:#1d3050;
  --dusk:#b0581a;
  --gold:#f2dc7a;
  --rust:#7b3a09;
  --rust-dark:#4a2205;
  --panel:rgba(92,88,84,.88);
  --panel-main:rgba(90,86,82,.72);
  --ink:#ffffff;
  --muted:#b8b4ae;
  --logo-bg:#1f1b18;
}
*{box-sizing:border-box;margin:0;padding:0}
html,body{width:1200px;height:832px;overflow:hidden;background:var(--night)}
.page{
  position:relative;width:1200px;height:832px;overflow:hidden;
  font-family:"Arimo",Arial,sans-serif;color:var(--ink);
  background:
    radial-gradient(ellipse 520px 170px at 600px 520px,rgba(214,128,40,.85),rgba(150,70,20,.5) 55%,transparent 100%),
    radial-gradient(ellipse 560px 320px at 600px 160px,rgba(48,72,112,.9),rgba(20,30,50,.6) 60%,transparent 100%),
    linear-gradient(180deg,#0e1726 0%,#1a2233 30%,#3a2414 55%,#1a0f08 80%,#040405 100%);
}
.page::after{
  content:"";position:absolute;inset:0;pointer-events:none;
  background:linear-gradient(90deg,#000 0%,rgba(0,0,0,.75) 9%,transparent 22%,transparent 78%,rgba(0,0,0,.75) 91%,#000 100%);
}
.site-nav{position:absolute;left:176px;top:18px;display:flex;gap:21px;z-index:2}
.site-nav a{color:var(--ink);text-decoration:none;font-weight:700;font-size:15px;letter-spacing:-.2px}
.site-title{position:absolute;left:171px;top:44px;z-index:2;font-size:40px;font-weight:700;color:var(--gold);letter-spacing:-.3px}
.sidebar{position:absolute;left:171px;top:117px;width:222px;height:574px;background:var(--panel);z-index:2}
.tab{
  position:absolute;left:-21px;width:222px;background:var(--rust);
  padding:11px 11px;font-size:14px;line-height:16px;color:var(--ink);letter-spacing:-.2px
}
.tab::after{
  content:"";position:absolute;left:0;bottom:-12px;width:0;height:0;
  border-top:12px solid var(--rust-dark);border-left:21px solid transparent;
}
.tab-intro{top:7px;height:54px}
.tab-subscribe{top:336px;height:53px}
.tab-social{top:483px;height:38px}
.brand-box{
  position:absolute;left:6px;top:69px;width:210px;height:141px;background:var(--logo-bg);
  display:flex;align-items:flex-end;justify-content:center;padding-bottom:26px
}
.brand-name{font-size:17px;color:var(--gold);font-weight:400;text-align:center;line-height:19px}
.tagline{position:absolute;left:6px;top:228px;width:212px;font-style:italic;font-size:11.6px;line-height:17px;text-align:center}
.email-label{position:absolute;left:6px;top:402px;font-size:10px}
.email-input{position:absolute;left:6px;top:413px;width:202px;height:27px;background:#fff;border:none}
.signup{position:absolute;left:8px;top:446px;width:51px;height:21px;border:1px solid #fff;background:transparent;color:#fff;font:700 10px "Arimo",Arial,sans-serif}
.social-dot{position:absolute;left:6px;top:531px;width:28px;height:28px;border-radius:50%;background:#3b5b9c}
.content{position:absolute;left:402px;top:117px;width:622px;height:590px;background:var(--panel-main);z-index:2}
.hero{
  position:absolute;left:6px;top:6px;width:611px;height:319px;
  background:linear-gradient(90deg,#3a3a3a 0%,#8a8a8a 30%,#5a5a5a 55%,#101010 75%,#0a0a0a 100%)
}
.hero-caption{
  position:absolute;left:370px;top:134px;font-family:"Cinzel",Georgia,serif;font-size:29px;line-height:32px;color:#fff;letter-spacing:.5px
}
.copy{position:absolute;left:14px;top:330px;width:600px;font-size:14px;line-height:16px;letter-spacing:-.25px}
.copy h2{font-size:15px;text-align:center;font-weight:700;line-height:17px}
.copy p{margin-bottom:16px}
.footer{position:absolute;left:0;width:1200px;top:720px;text-align:center;font-size:14px;color:var(--muted);z-index:2}
</style>
</head>
<body>
<div class="page">
  <nav class="site-nav">
    <a href="#">Home</a><a href="#">The 4 Key Questions</a><a href="#">Services</a><a href="#">About</a><a href="#">Contact</a><a href="#">Blog</a>
  </nav>
  <h1 class="site-title">Bluefern Capital Counsel LLC</h1>

  <aside class="sidebar">
    <div class="tab tab-intro">Quiet Harbor Chronicle for Social Impact Investors</div>
    <div class="brand-box"><span class="brand-name">Bluefern Capital Counsel</span></div>
    <p class="tagline">We show non-profit organizations and for-profit social enterprises … who are searching for growth capital funding … how to win the attention of social impact investors and make it to the second round of "due diligence."</p>
    <div class="tab tab-subscribe">Subscribe to Our Blog:<br>"Quiet Harbor Chronicle"</div>
    <label class="email-label" for="email">Email Address</label>
    <input class="email-input" id="email" type="text">
    <button class="signup" type="button">SIGN-UP</button>
    <div class="tab tab-social">Follow Us on Friendwall!</div>
    <span class="social-dot"></span>
  </aside>

  <main class="content">
    <div class="hero" role="img" aria-label="Black and white portrait of two smiling men in suits and bow ties">
      <div class="hero-caption">QUIET HARBOR<br>CHRONICLE</div>
    </div>
    <div class="copy">
      <h2>The Good News</h2>
      <p>In the United States, a powerful "social capital marketplace" is forming to fund the growth of high-impact social purpose organizations with proven solutions to challenging social, economic, or environmental problems.</p>
      <h2>The Bad News</h2>
      <p>Investors and funders in this marketplace ask tough questions in their search for solutions that "move the needle." To pass due diligence, you must provide two things: (1) evidence that your organization has the "entrepreneurial mindset" to execute a growth strategy, and (2) a high-quality social impact business plan with answers to four key questions.</p>
      <h2>The Opportunity</h2>
      <p>On average, only 1 out of 4 requests for growth capital make it to the second round of due diligence. We can show you how to win the attention of social impact investors and "make the cut." It's your call … will it be a rejection letter or a significant check to change more lives?</p>
    </div>
  </main>

  <footer class="footer">© 2014 BLUEFERN CAPITAL COUNSEL LLC. ALL RIGHTS RESERVED.</footer>
</div>
</body>
</html>
```